Graphic Design Project

I need to create a graphic design, which needs to be editable for me in Powerpoint... I have attached it a draft of it, but I need to be able to change the text of it. I want it to look more professional
Updates

Target Market(s)

Business Executives

Industry/Entity Type

Graphic Design

Requirements
Must have
• Make it look professional; the colors can change; I just need to be able to edit the text in powerpoint or either word

```html
<!DOCTYPE html>
<html lang="en">
<head>
<meta charset="utf-8">
<title>IT Leadership Framework</title>
<link href="https://fonts.googleapis.com/css2?family=Carlito:wght@400;700&display=swap" rel="stylesheet">
<style>
  :root {
    --bg: #ffffff;
    --khaki-top: #e0d38d;
    --khaki-bottom: #a89a4f;
    --green-top: #7cc47c;
    --green-bottom: #3c873c;
    --pink-top: #f7b7b9;
    --pink-bottom: #c97b7f;
    --taupe-top: #d3ccba;
    --taupe-bottom: #978f7b;
    --blue-top: #acdcec;
    --blue-bottom: #5ea6c0;
    --label: #ffffff;
    --banner-top: #f4f4f4;
    --banner-bottom: #c9c9c9;
    --banner-edge: #a9a9a9;
    --change-red: #e8141b;
  }
  * { margin: 0; padding: 0; box-sizing: border-box; }
  html, body {
    width: 1200px;
    height: 901px;
    overflow: hidden;
    background: var(--bg);
  }
  .canvas {
    position: relative;
    width: 1200px;
    height: 901px;
    font-family: "Carlito", "Calibri", sans-serif;
  }
  .block {
    position: absolute;
    width: 213px;
    height: 150px;
    border-radius: 26px 5px 26px 5px;
    display: flex;
    align-items: center;
    justify-content: center;
    text-align: center;
    color: var(--label);
    font-weight: 700;
    font-size: 22px;
    line-height: 1.5;
    padding: 8px 14px;
    text-shadow: 0 1px 2px rgba(0,0,0,0.25);
    box-shadow: 3px 5px 8px rgba(0,0,0,0.28), inset 0 2px 0 rgba(255,255,255,0.35);
    border: 1px solid rgba(0,0,0,0.08);
  }
  .block--khaki { background: linear-gradient(to bottom, var(--khaki-top), var(--khaki-bottom)); }
  .block--green { background: linear-gradient(to bottom, var(--green-top), var(--green-bottom)); }
  .block--pink  { background: linear-gradient(to bottom, var(--pink-top), var(--pink-bottom)); }
  .block--taupe { background: linear-gradient(to bottom, var(--taupe-top), var(--taupe-bottom)); }
  .block--blue  { background: linear-gradient(to bottom, var(--blue-top), var(--blue-bottom)); }
  .block small { font-size: 20px; }

  .foundation {
    position: absolute;
    left: 108px;
    top: 676px;
    width: 936px;
    height: 76px;
  }
  .foundation__label {
    position: absolute;
    left: 108px;
    top: 686px;
    width: 936px;
    text-align: center;
    font-size: 41px;
    font-weight: 400;
    color: var(--change-red);
    letter-spacing: 0.5px;
  }
</style>
</head>
<body>
<main class="canvas">
  <div class="block block--blue"  style="left:112px; top:506px;">Customer<br>Engagement<br>Model</div>
  <div class="block block--pink"  style="left:351px; top:506px;">Service-<br>Minded<br>IT Culture</div>
  <div class="block block--green" style="left:591px; top:506px;"><span>Policy, Process<br>&amp; <small>Methodologies</small></span></div>
  <div class="block block--taupe" style="left:824px; top:506px;">Meaningful<br>Metrics</div>

  <div class="block block--khaki" style="left:256px; top:361px;">Transform IT<br>Team</div>
  <div class="block block--taupe" style="left:504px; top:361px;">Master<br>Relationship<br>Management</div>
  <div class="block block--blue"  style="left:742px; top:359px;">Market &amp;<br>Communicate<br>Value</div>

  <div class="block block--green" style="left:397px; top:220px;">Maintain IT<br>Operational<br>Excellence</div>
  <div class="block block--pink"  style="left:651px; top:220px;">Create<br>Business Value</div>

  <div class="block block--khaki" style="left:530px; top:78px;">IT VISION &amp;<br>LEADERSHIP</div>

  <svg class="foundation" viewBox="0 0 936 76" aria-hidden="true">
    <defs>
      <linearGradient id="bannerFill" x1="0" y1="0" x2="0" y2="1">
        <stop offset="0" stop-color="var(--banner-top)"/>
        <stop offset="1" stop-color="var(--banner-bottom)"/>
      </linearGradient>
    </defs>
    <polygon points="3,3 933,3 758,73 186,73" fill="url(#bannerFill)" stroke="var(--banner-edge)" stroke-width="1.5"/>
  </svg>
  <div class="foundation__label">MANAGING CHANGE</div>
</main>
</body>
</html>
```